Knockdown rebuild flyer - SIZE DL

Wanting a brochure with similar layout attached with images provided.
Left hand side
REBUILD WITH MERIDAN

Running down the page
step 1: Design
design your dream home.
step 2: Select
personalise your new home
step 3:Demolish
it's in the title
step 4:Build
watch your dream take shape
step 5:Live
move into your new dream home and build new memories

bottom left
Contact: Tom Varga- 0427315540 -Tom@meridanhomes.example.au

house image similar to the attached example, Mhc logo top right corner.

Target Market(s)

knockdown rebuild clients

Industry/Entity Type

new home building

Font styles to use
Other font styles liked:
• melbourne

Requirements
Nice to have
• attached image

```html
<!DOCTYPE html>
<html lang="en">
<head>
<meta charset="utf-8">
<title>Rebuild with Meridan – Knockdown Rebuild Flyer</title>
<link rel="stylesheet" href="https://fonts.googleapis.com/css2?family=Abel&display=swap">
<style>
  :root {
    --navy: #1f3a5f;
    --slate: #8191a6;
    --slate-light: #a9b4c3;
    --slate-band: #7f8ea3;
    --white: #ffffff;
    --ink: #1e2f4a;
    --sky-top: #4fb4ea;
    --sky-bottom: #9fd4f2;
    --house-dark: #3b3f46;
    --ground: #9a9b98;
  }
  * { margin: 0; padding: 0; box-sizing: border-box; }
  html, body { width: 1200px; height: 578px; overflow: hidden; background: var(--white); }
  .flyer {
    position: relative;
    width: 1200px;
    height: 578px;
    overflow: hidden;
    font-family: "Abel", "Arial Narrow", sans-serif;
  }
  .flyer__shapes { position: absolute; inset: 0; }
  .headline {
    position: absolute;
    left: 40px;
    top: 98px;
    color: var(--white);
    font-size: 45px;
    font-weight: 400;
    letter-spacing: 2px;
    word-spacing: 6px;
    line-height: 1;
    white-space: nowrap;
  }
  .steps {
    position: absolute;
    left: 44px;
    top: 199px;
    list-style: none;
    color: var(--white);
    font-size: 23px;
    line-height: 34px;
    letter-spacing: 0.4px;
  }
  .steps li { display: flex; white-space: nowrap; }
  .steps__num { width: 79px; flex: none; }
  .contact-line {
    position: absolute;
    left: 42px;
    top: 472px;
    color: var(--ink);
    font-size: 29px;
    line-height: 1;
    white-space: nowrap;
  }
  .email-line {
    position: absolute;
    left: 42px;
    top: 517px;
    color: var(--white);
    font-size: 29px;
    line-height: 1;
    white-space: nowrap;
  }
  .brand-name {
    position: absolute;
    right: 46px;
    top: 38px;
    color: var(--white);
    font-size: 30px;
    letter-spacing: 3px;
    line-height: 1;
    white-space: nowrap;
  }
</style>
</head>
<body>
<main class="flyer">
  <svg class="flyer__shapes" width="1200" height="578" viewBox="0 0 1200 578">
    <defs>
      <linearGradient id="sky" x1="0" y1="0" x2="0" y2="1">
        <stop offset="0" stop-color="var(--sky-top)"/>
        <stop offset="0.45" stop-color="var(--sky-bottom)"/>
        <stop offset="0.46" stop-color="var(--house-dark)"/>
        <stop offset="0.8" stop-color="#6c7078"/>
        <stop offset="1" stop-color="var(--ground)"/>
      </linearGradient>
    </defs>
    <rect x="0" y="0" width="1200" height="107" fill="var(--slate)"/>
    <rect x="0" y="107" width="1200" height="32" fill="var(--white)"/>
    <rect role="img" aria-label="Photograph of a modern single-storey home with skillion roof, dark and white render, driveway and young trees under a blue sky" x="430" y="139" width="770" height="439" fill="url(#sky)"/>
    <polygon points="585,0 460,578 433,578" fill="var(--slate-light)" opacity="0.6"/>
    <polygon points="0,0 585,0 433,578 0,578" fill="var(--navy)"/>
    <polygon points="0,462 455,462 443,508 0,508" fill="var(--white)"/>
    <polygon points="0,513 441,513 424,578 0,578" fill="var(--slate-band)"/>
  </svg>

  <h1 class="headline">REBUILD WITH MERIDAN</h1>

  <ol class="steps">
    <li><span class="steps__num">STEP 1:</span><span>Design design your dream home</span></li>
    <li><span class="steps__num">STEP 2:</span><span>Select personalise your new home</span></li>
    <li><span class="steps__num">STEP 3:</span><span>Demolish it's in the title</span></li>
    <li><span class="steps__num">STEP 4:</span><span>Build watch your dream take shape</span></li>
    <li><span class="steps__num">STEP 5:</span><span>Live move into your new dream<br>home and build new memories</span></li>
  </ol>

  <p class="contact-line">Contact: Tom Varga- 0427315540</p>
  <p class="email-line">Tom@meridanhomes.example.au</p>

  <p class="brand-name">MERIDAN HOMES</p>
</main>
</body>
</html>
```